Legal Service Estimated Retainer and Average Case Value

We need an 11x14 flyer that contains the standard retainers and average cost be case, both provided in documents, for each case type we handle. We need the information displayed, preferably in a way that makes the information readable but less troubling to a client shocked at price of litigation. We need one sheet with the retainers and average case value merged into one table.

Target Market(s)

Potential Clients

Font styles to use
Serif
Sans Serif

```html
<!DOCTYPE html>
<html lang="en">
<head>
<meta charset="utf-8">
<title>Average Fee Per Case Type</title>
<link rel="stylesheet" href="https://fonts.googleapis.com/css2?family=Poppins:wght@400;600;700;800&family=Libre+Baskerville&display=swap">
<style>
  :root {
    --brand-blue: #1c3f93;
    --ink-navy: #14224f;
    --row-grey: #e7e7ea;
    --paper: #ffffff;
    --backdrop: #2b2b2d;
    --body-text: #1d1d24;
  }
  * { box-sizing: border-box; margin: 0; padding: 0; }
  html, body { width: 1200px; height: 1128px; overflow: hidden; background: var(--backdrop); }
  .canvas { position: relative; width: 1200px; height: 1128px; }
  .flyer {
    position: absolute; left: 176px; top: 24px;
    width: 1156px; height: 1471px;
    background: var(--paper);
    transform: scale(0.7342); transform-origin: 0 0;
    font-family: "Poppins", sans-serif; color: var(--ink-navy);
    box-shadow: 0 20px 60px rgba(0,0,0,.45);
  }
  .top-rule { position: absolute; left: 0; top: 0; width: 100%; height: 18px; background: var(--brand-blue); }
  .bottom-rule { position: absolute; left: 0; bottom: 0; width: 100%; height: 9px; background: var(--brand-blue); }
  .title-band {
    position: absolute; right: 0; top: 0; width: 510px; height: 155px;
    background: var(--brand-blue);
    border-bottom-left-radius: 70px;
    display: flex; flex-direction: column; justify-content: center; align-items: flex-end;
    padding: 10px 48px 0 0;
  }
  .title-band h1 { color: #fff; font-weight: 800; font-size: 51px; line-height: 50px; text-align: right; letter-spacing: .5px; }
  .firm-name { position: absolute; left: 56px; top: 56px; display: flex; align-items: center; gap: 18px; }
  .firm-square { width: 34px; height: 34px; background: var(--brand-blue); }
  .firm-text { font-family: "Libre Baskerville", serif; color: var(--ink-navy); font-weight: 400; }
  .firm-text .small { display: block; font-size: 19px; letter-spacing: .5px; }
  .firm-text .large { display: block; font-size: 38px; line-height: 44px; }
  .intro {
    position: absolute; left: 43px; top: 178px; width: 1072px;
    font-size: 19.5px; line-height: 28px; color: var(--body-text); font-weight: 400;
  }
  .fee-table { position: absolute; left: 43px; width: 1067px; list-style: none; }
  .fee-table.averages { top: 282px; }
  .fee-table.retainers { top: 916px; }
  .fee-row { display: flex; justify-content: space-between; align-items: center; height: 35px; font-weight: 700; font-size: 19.5px; }
  .fee-row:nth-child(odd) { height: 44px; background: var(--row-grey); }
  .fee-row .case { padding-left: 28px; }
  .fee-row .amount { width: 227px; height: 100%; display: flex; align-items: center; justify-content: flex-end; padding-right: 25px; }
  .fee-row:nth-child(odd) .amount { background: var(--brand-blue); color: #fff; clip-path: polygon(9px 0, 100% 0, 100% 100%, 0 100%); }
  .section-heading {
    position: absolute; left: 0; width: 100%; top: 826px; text-align: center;
    color: var(--brand-blue); font-weight: 800; font-size: 44px; letter-spacing: .3px;
  }
</style>
</head>
<body>
<div class="canvas">
  <article class="flyer">
    <div class="top-rule"></div>
    <div class="title-band"><h1>AVERAGE FEE<br>PER CASE TYPE</h1></div>
    <div class="firm-name">
      <span class="firm-square"></span>
      <span class="firm-text"><span class="small">THE LAW OFFICE OF</span><span class="large">MARTIN L WHITAKER</span></span>
    </div>
    <p class="intro">In order for our clients to set expectations for legal fees, we provide the national average range of fees per case type. These are only to provide you with an understanding of what other cases have cost clients in similar cases. Please note these are not estimates nor guarantees of your own legal costs.</p>

    <ul class="fee-table averages">
      <li class="fee-row"><span class="case">Custody Contempt/Modification</span><span class="amount">$5,000 - $8,000</span></li>
      <li class="fee-row"><span class="case">Custody Initial Order</span><span class="amount">$4,000 - $7,000</span></li>
      <li class="fee-row"><span class="case">Custody &amp; Support</span><span class="amount">$5,000 - $8,000</span></li>
      <li class="fee-row"><span class="case">Support</span><span class="amount">$2,000 - $4,000</span></li>
      <li class="fee-row"><span class="case">Divorce (3301c)</span><span class="amount">$1,500 - $3,000</span></li>
      <li class="fee-row"><span class="case">Divorce (3301d)</span><span class="amount">$2,000 - $3,000</span></li>
      <li class="fee-row"><span class="case">Protection from Abuse</span><span class="amount">$1,500 - $3,000</span></li>
      <li class="fee-row"><span class="case">Divorce &amp; Custody</span><span class="amount">$5,000 - $8,000</span></li>
      <li class="fee-row"><span class="case">Divorce &amp; Equitable Distribution</span><span class="amount">$6,000 - $10,000</span></li>
      <li class="fee-row"><span class="case">Divorce, Custody &amp; Support</span><span class="amount">$8,000 - $12,000</span></li>
      <li class="fee-row"><span class="case">Divorce, Equitable Distribution &amp; Custody</span><span class="amount">$10,000 - $15,000</span></li>
      <li class="fee-row"><span class="case">Divorce, Equitable Distribution &amp; Support</span><span class="amount">$8,000 - $12,000</span></li>
      <li class="fee-row"><span class="case">Divorce, Equitable Distribution, Custody &amp; Support</span><span class="amount">$12,000 - $15,000</span></li>
    </ul>

    <h2 class="section-heading">RETAINERS AND TOTAL ESTIMATED CASE COSTS</h2>

    <ul class="fee-table retainers">
      <li class="fee-row"><span class="case">Divorce (3301 C)</span><span class="amount">Retainer: $2,000</span></li>
      <li class="fee-row"><span class="case">Divorce (3301 D)</span><span class="amount">Retainer: $2,500</span></li>
      <li class="fee-row"><span class="case">Divorce and Custody</span><span class="amount">Retainer: $3,500</span></li>
      <li class="fee-row"><span class="case">Divorce and Equitable Distribution</span><span class="amount">Retainer: $3,500</span></li>
      <li class="fee-row"><span class="case">Divorce and Support</span><span class="amount">Retainer: $3,000</span></li>
      <li class="fee-row"><span class="case">Divorce, Custody and Support</span><span class="amount">Retainer: $3,500</span></li>
      <li class="fee-row"><span class="case">Divorce, Equitable Distribution and Support</span><span class="amount">Retainer: $3,500</span></li>
      <li class="fee-row"><span class="case">Divorce, Equitable Distribution and Custody</span><span class="amount">Retainer: $5,000</span></li>
      <li class="fee-row"><span class="case">Divorce, Equitable Distribution, Custody and Support</span><span class="amount">Retainer: $3,500</span></li>
      <li class="fee-row"><span class="case">Custody Initial Order</span><span class="amount">Retainer: $3,000</span></li>
      <li class="fee-row"><span class="case">Custody Modification</span><span class="amount">Retainer: $3,500</span></li>
      <li class="fee-row"><span class="case">Custody and Support</span><span class="amount">Retainer: $3,000</span></li>
      <li class="fee-row"><span class="case">(PFA) Protection From Abuse</span><span class="amount">Paid In Full: $2,000</span></li>
    </ul>
    <div class="bottom-rule"></div>
  </article>
</div>
</body>
</html>
```